Seafood company needs a label design

Our brand name is Coral Pilchards. We need a label design for a new product line of 200g trays of sardine fillets. The label/sleeve is going to wrap around the black tray. We are a family owned and operated business in Esperance, Western Australia. We would like simple appealing designs that catch the eye of the consumer.

Target Market(s)

seafood consumers in supermarkets

Colors

Designer to choose colors to be used in the design.

Requirements
Must have
• The front of the label must include
• •Coral Pilchards
• •since 1997
• •Sustainably wild caught from the pristine southern ocean Esperance Western Australia
Nice to have
• Deep/Rich colours, and black, maybe Drawn picture of sardine/sardines or an anchor fast anchor.
Should not have
• cartoon images, not too cluttered

```html
<!DOCTYPE html>
<html lang="en">
<head>
<meta charset="utf-8">
<title>Coral Pilchards – Tray Sleeve</title>
<link href="https://fonts.googleapis.com/css2?family=Open+Sans:ital,wght@0,600;1,400;1,700&display=swap" rel="stylesheet">
<style>
  :root {
    --sleeve-black: #000000;
    --ocean-blue: #1aa6e4;
    --text-white: #ffffff;
    --page-bg: #ffffff;
  }
  html, body {
    margin: 0;
    padding: 0;
    width: 1200px;
    height: 1200px;
    overflow: hidden;
    background: var(--page-bg);
  }
  .canvas {
    position: relative;
    width: 1200px;
    height: 1200px;
  }
  .sleeve {
    position: absolute;
    left: 50px;
    top: 344px;
    width: 1100px;
    height: 513px;
  }
  .sleeve-bg { fill: var(--sleeve-black); }
  .edge-band { fill: var(--ocean-blue); }
  .flag { fill: var(--ocean-blue); }
  .tagline {
    font-family: "Open Sans", sans-serif;
    font-style: italic;
    font-size: 26px;
    fill: var(--text-white);
  }
  .tagline .strong { font-weight: 700; }
  .tagline .soft { font-weight: 400; }
  .brand-name {
    font-family: "Open Sans", sans-serif;
    font-weight: 600;
    font-size: 76px;
    letter-spacing: 4px;
    fill: var(--ocean-blue);
  }
  .since-tag {
    font-family: "Open Sans", sans-serif;
    font-weight: 600;
    font-size: 22px;
    fill: var(--text-white);
  }
</style>
</head>
<body>
<div class="canvas">
  <svg class="sleeve" viewBox="0 0 1100 513" xmlns="http://www.w3.org/2000/svg">
    <rect class="sleeve-bg" x="0" y="0" width="1100" height="513"/>
    <rect class="edge-band" x="0" y="8" width="1100" height="12"/>
    <rect class="edge-band" x="0" y="493" width="1100" height="12"/>

    <text class="tagline" x="29" y="72">
      <tspan class="strong">Sustainably Wild Caught</tspan><tspan class="soft"> from the </tspan><tspan class="strong">Pristine</tspan>
    </text>
    <text class="tagline" x="29" y="110">
      <tspan class="strong">Southern Ocean Esperance Western Australia</tspan>
    </text>

    <text class="brand-name" x="560" y="300" text-anchor="middle">CORAL PILCHARDS</text>

    <polygon class="flag" points="906,414 1077,414 1077,448 906,448 916,431"/>
    <text class="since-tag" x="996" y="439" text-anchor="middle">SINCE 1997</text>
  </svg>
</div>
</body>
</html>
```